かなり豪華な(市販価格1,890円)フルカラーのカタログを自社製作しており、
それをホームページ上で無料でプレゼントしています。
現在はこのようなページになっています。
http://www.tamasou-niwa.com/contact/
いろいろな資料が同時に請求できるようになっていますが、
今回依頼したいのは、施工事例カタログ専用のランディングページです。

イメージは、森市のヒット商品の販売ページみたいな感じです。
(安っぽいデザインのページが多いので、もっと高級感を出したいですが)
こちらのサイトでいろいろ作例が載っていました。
http://www.hanaso-works.jp/theme18.html

こんな感じも好きです。
http://bemoto.co.jp/recruit/legend-designer/

1ページの構成にしたいですが、
あまりタテに長く作りたくありません。
モニター2画面分くらいで収めたいです。

カタログの特徴はこちらです。
■フルカラー・300ページ。
■エクステリアの施工例に特化したカタログは希少。
■価格が載っているので、自宅を工事する場合の金額のイメージが付けやすい。
■定価1890円でポルカスで販売中のものが無料でもらえる。

http://www.tamasou-niwa.com/
1ページ
グリーン・ベージュ・ブラウン・ブラック
• 高解像度JPG (.jpg)
• イラストレーター形式 (.ai)
古いカタログの画像ですが、製作用の参考に添付しておきます。
http://okuribin.jp/download/1f0e2d3c4b5a69788796a5b4c3d2e1f0a9b8c7d6

画像等の素材もアップしました。
http://okuribin.jp/download/2e1f3a4b5c6d7e8f9a0b1c2d3e4f5a6b7c8d9e0f
http://okuribin.jp/download/3d2c1b0a9f8e7d6c5b4a3f2e1d0c9b8a7f6e5d4c

ご提案の際はダミーのカタログ画像などで行っていただき、
当選の方には実際のカタログをご送付し、最終的に仕上げていただきます。
よろしくお願いします。
訴求のポイントについてご質問いただきましたので、
一つ付け加えたいと思います。

「制作費が非常に高いため、在庫が無くなり次第終了です」
というような言葉をつかっていただけますか?
※言い方はこの通りでなくてもOKです。

今回のページはリスティング広告用のランディングページになりますので、資料請求(=カタログの無料プレゼントへの申し込み)をしてもらうことが最大の目的です。そのためには、無料であること、豪華なこと、内容が濃いことなどを訴求していただければと思います。

よろしくお願いします。
よろしくお願いします。
>1ページの構成にしたいですが、
>あまりタテに長く作りたくありません。
>モニター2画面分くらいで収めたいです。

依頼内容にこのように記載しましたが、
これは無視していただいてかまいません。
※どれだけタテに長くなってもOKです。
ご提案ありがとうございます。
一つ注意点があります。
サイト訪問者に動作をしてもらうようなページはNGでお願いします。
(クリックしてページをめくるなど)
動作に凝らなくい方がいいですし、ビジュアルも然りです。
単純にこの一覧のようなページでかまいません。
http://www.peji-narabe.jp/
よろしくお願いします。
素材のアップロード期限が過ぎてしまったため、
こちらに再アップしました。

http://okuribin.jp/download/4c5d6e7f8a9b0c1d2e3f4a5b6c7d8e9f0a1b2c3d

http://okuribin.jp/download/5b6a7f8e9d0c1b2a3f4e5d6c7b8a9f0e1d2c3b4a

http://okuribin.jp/download/6a7b8c9d0e1f2a3b4c5d6e7f8a9b0c1d2e3f4a5b

よろしくお願いします。

デザインの第一印象がとてもよく、コンテンツも見やすくまとまっており、高いコンバージョンが期待できる作品だと思いました。

魅力的なご提案をありがとうございました。
こういったデザインコンペは今後も複数依頼予定ですので、次回もよろしくお願いします。

```html
<!DOCTYPE html>
<html lang="ja">
<head>
<meta charset="utf-8">
<title>緑苑工房 施工カタログ無料キャンペーン</title>
<link rel="stylesheet" href="https://fonts.googleapis.com/css2?family=Noto+Sans+JP:wght@400;700&family=Noto+Serif+JP:wght@400;700&display=swap">
<style>
:root{
  --black:#0c0a08;
  --ink:#16120e;
  --brown:#3b2a1b;
  --brown-dark:#241910;
  --gold:#c9a962;
  --gold-light:#e7d3a0;
  --beige:#ece3d2;
  --red:#b3141b;
  --red-dark:#8a0e13;
  --grey:#8a8580;
  --white:#ffffff;
  --line:#cfc6b6;
}
*{box-sizing:border-box;margin:0;padding:0}
html,body{width:1200px;height:4384px;overflow:hidden;background:var(--black)}
body{font-family:"Noto Sans JP",sans-serif;color:var(--white);position:relative}
section,header,footer{position:absolute;left:0;width:1200px}
.photo{position:absolute;border:3px solid #f2efe8}

/* header */
.site-header{top:0;height:460px;background:var(--black)}
.brand{position:absolute;left:60px;top:26px;display:flex;align-items:center;gap:12px}
.brand-mark{width:50px;height:50px;border-radius:50%;background:var(--beige)}
.brand-name{font-family:"Noto Serif JP",serif;font-weight:700;font-size:30px;color:var(--white)}
.tagline{position:absolute;left:270px;top:14px;font-family:"Noto Serif JP",serif;font-size:30px;line-height:1.25}
.tagline small{display:block;font-size:17px;color:var(--beige);margin-top:2px}
.contact-top{position:absolute;right:60px;top:16px;font-size:14px;color:var(--beige);line-height:1.5}
.contact-top .tel{font-size:34px;font-weight:700;color:var(--white);letter-spacing:1px;display:flex;align-items:center;gap:8px;line-height:1.2}
.contact-top .mail{font-size:15px;display:flex;align-items:center;gap:8px}
.hero-photo{position:absolute;left:0;top:110px;width:1200px;height:350px;background:radial-gradient(ellipse at 60% 45%,#6b4a28 0%,#2a1d12 45%,#090706 85%)}
.hero-copy{position:absolute;left:0;top:360px;width:1200px;text-align:center;font-family:"Noto Serif JP",serif}
.hero-copy .lead{font-size:15px;color:var(--beige);margin-bottom:6px}
.hero-copy .main{font-size:36px;font-weight:700;white-space:nowrap}
.hero-copy .main em{font-style:normal;font-size:44px;color:var(--gold-light)}

/* catalog offer */
.offer{top:460px;height:360px;background:linear-gradient(#1e1610,#0e0b08)}
.offer-title{position:absolute;left:230px;top:20px;width:740px;height:56px;border:2px solid var(--gold);background:#fbf8f1;color:var(--ink);font-family:"Noto Serif JP",serif;font-weight:700;font-size:28px;text-align:center;line-height:52px}
.offer-book{left:220px;top:110px;width:330px;height:200px;background:linear-gradient(135deg,#6b5032,#2c2015);border:none;transform:skewX(-6deg)}
.offer-text{position:absolute;left:600px;top:110px;font-family:"Noto Serif JP",serif}
.offer-text .price{font-size:17px;color:var(--beige)}
.offer-text .free{font-size:36px;font-weight:700;margin-top:6px}
.btn{display:block;text-align:center;color:var(--white);font-weight:700;font-size:20px;border-radius:4px;text-decoration:none}
.btn-red{background:linear-gradient(var(--red),var(--red-dark));box-shadow:0 3px 0 #4d070a}
.btn-brown{background:linear-gradient(#5b4129,var(--brown-dark));box-shadow:0 3px 0 #120c07}
.offer .btn{position:absolute;left:620px;top:220px;width:360px;height:52px;line-height:52px}

/* intro */
.intro{top:820px;height:100px;text-align:center;font-family:"Noto Serif JP",serif;font-size:22px;line-height:1.7;padding-top:18px}

/* gallery */
.gallery{top:920px;height:790px;background:var(--black)}
.gallery .photo{border-color:#e8e4dc}
.g1{left:190px;top:20px;width:230px;height:120px;background:linear-gradient(#c9c4ba,#7e7566)}
.g2{left:440px;top:20px;width:560px;height:320px;background:linear-gradient(160deg,#d9d3c5,#6a5a44)}
.g3{left:190px;top:170px;width:240px;height:210px;background:linear-gradient(#4a3523,#120c08)}
.g4{left:450px;top:360px;width:300px;height:200px;background:linear-gradient(#6d5f4b,#2b2218)}
.g5{left:780px;top:360px;width:220px;height:150px;background:linear-gradient(#d8cfbd,#8c7c63)}
.g6{left:190px;top:400px;width:240px;height:140px;background:linear-gradient(#3a2a1b,#0d0906)}
.g7{left:540px;top:560px;width:300px;height:190px;background:linear-gradient(#e8e1d2,#8f7c60)}
.g8{left:850px;top:530px;width:150px;height:130px;background:linear-gradient(#4a3a28,#19120c)}
.g9{left:190px;top:580px;width:300px;height:180px;background:linear-gradient(#6a4a26,#1a110a)}
.label{position:absolute;background:var(--white);color:var(--ink);font-size:12px;padding:6px 10px;line-height:1.4}
.label-main{left:180px;top:230px;width:340px;padding:10px 14px;font-family:"Noto Serif JP",serif;font-size:12px;box-shadow:0 2px 6px rgba(0,0,0,.5)}
.label-main strong{display:block;font-size:28px;white-space:nowrap;line-height:1.35}
.label-main .sub{display:block;font-size:17px;font-weight:700}

/* tips */
.tips{top:1710px;height:190px;text-align:center}
.tips h2{font-family:"Noto Serif JP",serif;font-size:24px;font-weight:700;line-height:1.6}
.tips p{font-size:13px;color:var(--beige);line-height:1.9;margin-top:14px}

/* voice band */
.voice{top:1900px;height:390px;background:linear-gradient(#55514c,#3b3834)}
.voice-pages{left:230px;top:30px;width:400px;height:320px;background:linear-gradient(135deg,#f4f0e7,#bfb6a5)}
.voice-card{position:absolute;left:680px;top:70px;width:320px;height:250px;background:var(--black);padding:22px 24px;font-family:"Noto Serif JP",serif}
.voice-card .from{font-size:14px;color:var(--beige)}
.voice-card .body{font-size:24px;line-height:1.55;margin-top:8px;font-weight:700}

/* campaign */
.campaign{top:2300px;height:360px}
.campaign-box{position:absolute;left:200px;top:0;width:800px;height:360px;background:var(--black);border:1px solid #3b342c}
.badge{position:absolute;left:20px;top:18px;width:70px;height:70px;background:var(--red);color:var(--white);font-weight:700;font-size:16px;text-align:center;line-height:22px;padding-top:13px}
.campaign-head{position:absolute;left:110px;top:16px;font-size:15px;line-height:1.6}
.campaign-head .catch{font-family:"Noto Serif JP",serif;font-size:28px;font-weight:700;color:var(--gold-light)}
.campaign-photo{left:130px;top:120px;width:560px;height:215px;border:none;background:linear-gradient(90deg,#2a1e14,#6a4a2a 50%,#1a130d)}
.campaign-cover{position:absolute;left:430px;top:130px;width:260px;height:200px;background:var(--black);border:1px solid #444;padding:36px 28px;font-family:"Noto Serif JP",serif;font-size:24px;line-height:1.3;letter-spacing:2px}

/* order */
.order{top:2660px;height:240px}
.order .note{position:absolute;left:0;top:16px;width:1200px;text-align:center;font-size:13px;color:#e04a4f}
.order .cta{position:absolute;left:220px;top:70px;font-family:"Noto Serif JP",serif;font-size:15px;line-height:1.5}
.order .cta strong{font-size:26px}
.order .contact{position:absolute;left:640px;top:52px;font-size:13px;color:var(--beige);line-height:1.6}
.order .contact .tel{font-size:34px;font-weight:700;color:var(--white);display:flex;align-items:center;gap:8px;line-height:1.3}
.order .btn-red{position:absolute;left:220px;top:170px;width:370px;height:50px;line-height:50px}
.order .btn-brown{position:absolute;left:620px;top:170px;width:370px;height:50px;line-height:50px}

/* form */
.form-area{top:2910px;height:1270px}
.form-notes{position:absolute;left:200px;top:0;width:800px;font-size:13px;line-height:1.7;color:var(--beige)}
.form-panel{position:absolute;left:200px;top:70px;width:800px;height:1180px;background:var(--white);color:var(--ink);padding:28px 40px}
.form-panel .sub{text-align:center;font-size:14px}
.form-panel h2{text-align:center;font-family:"Noto Serif JP",serif;font-size:34px;font-weight:700;margin-top:2px;margin-bottom:22px}
.form-row{display:flex;border-top:1px solid var(--line);min-height:62px}
.form-row:last-of-type{border-bottom:1px solid var(--line)}
.form-row dt{width:150px;background:#f3efe7;font-size:14px;font-weight:700;padding:20px 14px}
.form-row dd{flex:1;padding:14px 18px;font-size:12px;color:var(--grey)}
.field{display:block;height:30px;border:1px solid #bdb6aa;background:#fcfbf8;width:300px;margin-bottom:6px}
.field.wide{width:480px}
.field.area{height:110px;width:480px}
.field.select{width:200px}
.form-panel .btn{width:360px;height:58px;line-height:58px;margin:36px auto 0;font-size:22px}

/* footer */
.site-footer{top:4190px;height:194px;background:var(--black);border-top:1px solid #2a241d}
.footer-name{position:absolute;left:60px;top:36px;font-family:"Noto Serif JP",serif;font-size:28px;font-weight:700}
.footer-name small{font-size:16px;font-weight:400}
.footer-desc{position:absolute;left:60px;top:90px;font-size:13px;line-height:1.8;color:var(--beige);width:760px}
.footer-contact{position:absolute;right:60px;top:40px;font-size:13px;color:var(--beige);line-height:1.6}
.footer-contact .tel{font-size:34px;font-weight:700;color:var(--white);display:flex;align-items:center;gap:8px;line-height:1.3}
.footer-contact .mail{display:flex;align-items:center;gap:8px;font-size:15px}
</style>
</head>
<body>

<header class="site-header">
  <div class="brand"><span class="brand-mark"></span><span class="brand-name">緑苑工房</span></div>
  <p class="tagline">毎月5件だけの<br>プレミアムガーデン。<small>～施工カタログ無料キャンペーン～</small></p>
  <div class="contact-top">
    <p>カタログ請求のお問い合わせ</p>
    <p class="tel"><svg width="34" height="24" viewBox="0 0 34 24"><rect x="1" y="1" width="32" height="22" rx="3" fill="#fff"/><text x="17" y="17" font-size="12" text-anchor="middle" fill="#000" font-family="sans-serif" font-weight="700">FREE</text></svg>0120-418-237</p>
    <p class="mail"><svg width="24" height="16" viewBox="0 0 24 16"><rect x="1" y="1" width="22" height="14" fill="none" stroke="#ece3d2" stroke-width="2"/><path d="M1 1l11 8 11-8" fill="none" stroke="#ece3d2" stroke-width="2"/></svg>info@ryokuen-kobo.jp</p>
  </div>
  <div class="hero-photo" role="img" aria-label="夜のライトアップに照らされた邸宅とエクステリアの写真"></div>
  <div class="hero-copy">
    <p class="lead">ネット上では、決して手に入らない本物の情報を、あなただけにお届けします。</p>
    <p class="main">本当の情報を知りたいあなたにだけに送る<em>プレミアムな</em>一冊。</p>
  </div>
</header>

<section class="offer">
  <h2 class="offer-title">エクステリア＆ガーデンの施工事例写真集</h2>
  <div class="photo offer-book" role="img" aria-label="開いた施工事例カタログの写真"></div>
  <div class="offer-text">
    <p class="price">定価1890円で販売中のカタログが</p>
    <p class="free">今なら無料でもらえます。</p>
  </div>
  <a class="btn btn-red" href="#form">無料カタログ申し込みフォームへ</a>
</section>

<section class="intro">
  <p>エクステリア・外構工事を行う方にとって最も重要なことは、<br>「正しい情報」に触れることです。</p>
</section>

<section class="gallery">
  <div class="photo g1" role="img" aria-label="外構工事の施工例写真"></div>
  <div class="photo g2" role="img" aria-label="ガーデンルームのある庭の施工例写真"></div>
  <div class="photo g3" role="img" aria-label="夜の門まわりの施工例写真"></div>
  <div class="photo g4" role="img" aria-label="植栽とウッドデッキの施工例写真"></div>
  <div class="photo g5" role="img" aria-label="庭の小物とテラスの写真"></div>
  <div class="photo g6" role="img" aria-label="ライトアップされたアプローチの写真"></div>
  <div class="photo g7" role="img" aria-label="明るいテラスの施工例写真"></div>
  <div class="photo g8" role="img" aria-label="照明付き外構の写真"></div>
  <div class="photo g9" role="img" aria-label="夜のエントランスの施工例写真"></div>
  <div class="label label-main">カタログ1冊に施工事例がぎっしり<strong>フルカラー・300ページ</strong><span class="sub">実際の施工事例イメージが満載！</span></div>
  <div class="label" style="left:800px;top:300px">カタログの内容は<br>施工事例の写真が満載です</div>
  <div class="label" style="left:230px;top:550px">あなたのイメージに近い施工例が<br>きっと見つかるはず</div>
  <div class="label" style="left:870px;top:680px">エクステリアの施工例に<br>特化したカタログは希少です</div>
</section>

<section class="tips">
  <h2>"エクステリア作りを成功させるコツは<br>「エクステリアの施工例を数多く見ること」です。"</h2>
  <p>これまでのガーデン工事で手がけた数多くの事例を、1冊のカタログにまとめました。<br>ひとつひとつの写真を見ることで、理想のお庭づくりのヒントがきっと見つかります。<br>カタログは無料でお届けします。まずはお気軽にお申し込みください。</p>
</section>

<section class="voice">
  <div class="photo voice-pages" role="img" aria-label="カタログの中面ページの写真"></div>
  <div class="voice-card">
    <p class="from">お客様からの意見が多い<br>嬉しいポイント</p>
    <p class="body">実際の価格やサービスの詳しい内容を見られるので自宅を工事する場合のイメージが付けやすい。</p>
  </div>
</section>

<section class="campaign">
  <div class="campaign-box">
    <div class="badge">数量<br>限定</div>
    <div class="campaign-head">エクステリア＆ガーデンの施工カタログ写真集<br>GARDEN &amp; EXTERIOR CATALOG
      <p class="catch">今だけ無料でプレゼントキャンペーン！</p>
    </div>
    <div class="photo campaign-photo" role="img" aria-label="カタログの表紙と施工写真の一覧"></div>
    <div class="campaign-cover">GARDEN<br>AND<br>EXTERIOR<br>CATALOG</div>
  </div>
</section>

<section class="order">
  <p class="note">※制作費が非常に高いため、在庫が無くなり次第終了となります。お早めにお申し込みください。</p>
  <p class="cta">エクステリア＆ガーデンの施工事例集<br><strong>無料カタログ申し込みはこちらから！</strong></p>
  <div class="contact">
    <p>電話・メールでのお申し込みも受け付けております</p>
    <p class="tel"><svg width="34" height="24" viewBox="0 0 34 24"><rect x="1" y="1" width="32" height="22" rx="3" fill="#fff"/><text x="17" y="17" font-size="12" text-anchor="middle" fill="#000" font-family="sans-serif" font-weight="700">FREE</text></svg>0120-418-237</p>
    <p>メール：info@ryokuen-kobo.jp</p>
  </div>
  <a class="btn btn-red" href="#form">無料カタログ申し込みフォームへ</a>
  <a class="btn btn-brown" href="#form">その他のカタログを見る</a>
</section>

<section class="form-area" id="form">
  <div class="form-notes">
    <p>※施工可能エリア外にお住まいの方にもカタログをお送りいたします。</p>
    <p>※カタログの発送はお申し込みから1週間ほどお時間をいただく場合がございます。</p>
  </div>
  <div class="form-panel">
    <p class="sub">エクステリア＆ガーデンの施工事例集</p>
    <h2>無料カタログ申し込みフォーム</h2>
    <dl>
      <div class="form-row"><dt>お名前</dt><dd><span class="field"></span>例）緑苑 太郎</dd></div>
      <div class="form-row"><dt>フリガナ</dt><dd><span class="field"></span>例）リョクエン タロウ</dd></div>
      <div class="form-row"><dt>メールアドレス</dt><dd><span class="field wide"></span>確認のためもう一度ご入力ください<span class="field wide"></span></dd></div>
      <div class="form-row"><dt>郵便番号</dt><dd><span class="field select"></span></dd></div>
      <div class="form-row"><dt>ご住所</dt><dd><span class="field select"></span><span class="field wide"></span></dd></div>
      <div class="form-row"><dt>電話番号</dt><dd><span class="field"></span></dd></div>
      <div class="form-row"><dt>工事予定時期</dt><dd><span class="field select"></span></dd></div>
      <div class="form-row"><dt>ご予算</dt><dd><span class="field select"></span></dd></div>
      <div class="form-row"><dt>ご検討内容</dt><dd><span class="field select"></span><span class="field wide"></span></dd></div>
      <div class="form-row"><dt>ご要望・ご質問</dt><dd><span class="field area"></span></dd></div>
    </dl>
    <a class="btn btn-red" href="#form">送信する</a>
  </div>
</section>

<footer class="site-footer">
  <p class="footer-name">緑苑工房<small>（りょくえんこうぼう）</small></p>
  <p class="footer-desc">エクステリア外構工事とガーデニング工事を専門に手がけるプロショップです。<br>地域に根ざした丁寧な施工で、理想のお庭づくりをお手伝いいたします。</p>
  <div class="footer-contact">
    <p>カタログ請求のお問い合わせ</p>
    <p class="tel"><svg width="34" height="24" viewBox="0 0 34 24"><rect x="1" y="1" width="32" height="22" rx="3" fill="#fff"/><text x="17" y="17" font-size="12" text-anchor="middle" fill="#000" font-family="sans-serif" font-weight="700">FREE</text></svg>0120-418-237</p>
    <p class="mail"><svg width="24" height="16" viewBox="0 0 24 16"><rect x="1" y="1" width="22" height="14" fill="none" stroke="#ece3d2" stroke-width="2"/><path d="M1 1l11 8 11-8" fill="none" stroke="#ece3d2" stroke-width="2"/></svg>info@ryokuen-kobo.jp</p>
  </div>
</footer>

</body>
</html>
```